Brisk Haven Womens Shaving Foam (For sale in supermarkets).

We supply supermarkets with various products and now need a new design for a Ladies Shaving Foam Can. Soft Pink on the bottom of the can finishing of gradated into white. Needs to have a Shaving Foam swirl image also needs to have our Brisk Haven Logo. White base Can with mainly soft pink. I have mocked one up with Brisk Haven Logo in the middle similar to the Body Spray cans. Good Luck.
Target Market(s)
Females
Industry/Entity Type
Grocery
Colors
ffffff
e34197
e667a6
eea4c8
f9d9e8
Requirements
Must have
- White Can base with Pink colour tones
Nice to have
- Modern fresh feel
Should not have
- No dark colours soft pinks

```html
<!DOCTYPE html>
<html lang="en">
<head>
<meta charset="utf-8">
<title>Brisk Haven Sensitive Shaving Foam – Label</title>
<link rel="stylesheet" href="https://fonts.googleapis.com/css2?family=Cinzel:wght@400;700;900&display=swap">
<style>
  :root {
    --white: #ffffff;
    --pink-deep: #e34197;
    --pink-mid: #e667a6;
    --pink-soft: #eea4c8;
    --pink-blush: #f9d9e8;
    --pink-brand: #e8206f;
    --cyan: #1aa6e4;
    --label-edge: #d6d6d6;
  }
  * { box-sizing: border-box; margin: 0; padding: 0; }
  html, body {
    width: 1200px; height: 1200px; overflow: hidden;
    background: var(--white);
  }
  .canvas {
    position: relative; width: 1200px; height: 1200px;
    background: var(--white);
  }
  .label {
    position: absolute; left: 331px; top: 40px;
    width: 538px; height: 1120px;
    border: 1px solid var(--label-edge);
    overflow: hidden;
    background: linear-gradient(to bottom,
      var(--white) 0%,
      var(--white) 58%,
      var(--pink-blush) 68%,
      var(--pink-soft) 80%,
      var(--pink-mid) 92%,
      #ee4f8c 100%);
  }
  .dancer-art {
    position: absolute; left: 81px; top: 31px;
    width: 376px; height: 733px;
    background: radial-gradient(ellipse at 50% 45%,
      rgba(238,164,200,0.55) 0%,
      rgba(249,217,232,0.45) 45%,
      rgba(255,255,255,0) 75%);
  }
  .brand {
    position: absolute; left: 0; right: 0; top: 420px;
    display: flex; align-items: center; justify-content: center; gap: 14px;
  }
  .brand-mark {
    width: 26px; height: 26px; background: var(--pink-brand);
  }
  .brand-name {
    font-family: "Cinzel", serif; font-weight: 900;
    font-size: 58px; color: var(--pink-brand);
    letter-spacing: 1px; line-height: 1;
  }
  .variant {
    position: absolute; left: 0; right: 0; top: 528px;
    text-align: center;
    font-family: "Cinzel", serif; font-weight: 400;
    font-size: 38px; color: var(--cyan); letter-spacing: 1px;
  }
  .foam-art {
    position: absolute; left: 173px; top: 774px;
    width: 193px; height: 156px;
    border-radius: 50% 50% 46% 46% / 62% 62% 38% 38%;
    background: radial-gradient(ellipse at 45% 40%,
      var(--white) 0%, var(--pink-blush) 55%, var(--pink-soft) 100%);
  }
  .skin-type {
    position: absolute; left: 0; right: 0; top: 945px;
    text-align: center;
    font-family: "Cinzel", serif; font-weight: 400;
    font-size: 30px; color: var(--cyan); letter-spacing: 1px;
  }
  .product-band {
    position: absolute; left: 40px; right: 40px; top: 988px; height: 62px;
    background: linear-gradient(to right,
      rgba(227,65,151,0) 0%, rgba(227,65,151,0.55) 30%,
      rgba(227,65,151,0.55) 70%, rgba(227,65,151,0) 100%);
    display: flex; align-items: center; justify-content: center;
  }
  .product-name {
    font-family: "Cinzel", serif; font-weight: 700;
    font-size: 40px; color: var(--white); letter-spacing: 0.5px;
  }
  .volume {
    position: absolute; left: 0; right: 0; top: 1060px;
    text-align: center;
    font-family: "Cinzel", serif; font-weight: 400;
    font-size: 22px; color: var(--cyan);
  }
</style>
</head>
<body>
  <main class="canvas">
    <section class="label">
      <div class="dancer-art" role="img" aria-label="Soft pink illustration of a dancing woman in a flowing dress"></div>

      <div class="brand">
        <span class="brand-mark"></span>
        <span class="brand-name">Brisk Haven</span>
      </div>

      <p class="variant">SOFT BLOOM</p>

      <div class="foam-art" role="img" aria-label="Swirl of white and pink shaving foam"></div>

      <p class="skin-type">SENSITIVE</p>

      <div class="product-band">
        <h1 class="product-name">SHAVING FOAM</h1>
      </div>

      <p class="volume">200 ml - 100g</p>
    </section>
  </main>
</body>
</html>
```